washable paper bags and accessories

We are three sisters who have discovered a mutual love of bags made from washable paper. It is a brand new business venture for bags, handbags, cosmetic bags, and home storage solutions and décor all made with washable paper.
We would like to have white crumpled paper as a background for both sides. Front of card with the words "plume douce cloth" only in "bohemian typewriter regular" font. Back of card with appointment style format for our next pop up stall
Target Market(s)
mums, females
Industry/Entity Type
Business
Contact Information for Business Card
ph: 0487215364
email:plumedoucecloth@mailbarrow.com

```html
<!DOCTYPE html>
<html lang="en">
<head>
<meta charset="utf-8">
<title>Plume Douce Cloth — Business Card</title>
<link href="https://fonts.googleapis.com/css2?family=Special+Elite&family=Courier+Prime:wght@400;700&display=swap" rel="stylesheet">
<style>
  :root {
    --page: #ffffff;
    --ink: #111111;
    --border: #1a1a1a;
    --band-dark: #3b3b3b;
    --band-mid: #595959;
    --band-light: #808080;
    --paper-light: #fbfcfc;
    --paper-mid: #eef1f1;
    --paper-shade: #dfe5e4;
    --rule: #333333;
  }
  * { margin: 0; padding: 0; box-sizing: border-box; }
  html, body {
    width: 1200px;
    height: 352px;
    overflow: hidden;
    background: var(--page);
  }
  .canvas {
    position: relative;
    width: 1200px;
    height: 352px;
  }
  .card {
    position: absolute;
    border: 1.5px solid var(--border);
    overflow: hidden;
  }
  .card--front { left: 3px; top: 0; width: 560px; height: 345px; }
  .card--back { left: 645px; top: 5px; width: 553px; height: 345px; }

  .paper-texture {
    position: absolute;
    inset: 0;
    background:
      radial-gradient(ellipse at 20% 30%, var(--paper-light) 0%, transparent 55%),
      radial-gradient(ellipse at 75% 70%, var(--paper-shade) 0%, transparent 60%),
      radial-gradient(ellipse at 60% 20%, var(--paper-mid) 0%, transparent 50%),
      linear-gradient(135deg, var(--paper-light), var(--paper-mid));
  }

  .bands {
    position: absolute;
    left: 0;
    right: 0;
    display: flex;
    flex-direction: column;
  }
  .bands span { display: block; height: 25px; }
  .bands--top { top: 0; }
  .bands--bottom { bottom: 0; }
  .band-dark { background: var(--band-dark); }
  .band-mid { background: var(--band-mid); }
  .band-light { background: var(--band-light); }

  .brand-name {
    position: absolute;
    left: 0;
    right: 0;
    top: 162px;
    text-align: center;
    font-family: "Special Elite", "Courier New", monospace;
    font-size: 33px;
    letter-spacing: 2px;
    color: var(--ink);
    text-transform: uppercase;
  }
  .contact-line {
    position: absolute;
    left: 0;
    right: 0;
    top: 285px;
    text-align: center;
    font-family: "Courier Prime", "Courier New", monospace;
    font-weight: 700;
    font-size: 13.5px;
    color: var(--ink);
  }

  .appointment-title {
    position: absolute;
    left: 0;
    right: 0;
    top: 38px;
    text-align: center;
    font-family: "Special Elite", "Courier New", monospace;
    font-size: 26px;
    letter-spacing: 2px;
    color: var(--ink);
  }
  .field {
    position: absolute;
    left: 48px;
    right: 36px;
    display: flex;
    align-items: flex-end;
    font-family: "Courier Prime", "Courier New", monospace;
    font-size: 17px;
    color: var(--ink);
  }
  .field--date { top: 107px; }
  .field--place { top: 162px; }
  .field-label { white-space: pre; }
  .field-line {
    flex: 1;
    margin-left: 12px;
    margin-bottom: 5px;
    border-bottom: 1.5px solid var(--rule);
  }
</style>
</head>
<body>
  <main class="canvas">
    <section class="card card--front">
      <div class="paper-texture" role="img" aria-label="White crumpled paper texture"></div>
      <div class="bands bands--top">
        <span class="band-dark"></span>
        <span class="band-mid"></span>
        <span class="band-light"></span>
      </div>
      <h1 class="brand-name">plume douce cloth</h1>
      <p class="contact-line">phone:0487215364 | email:plumedoucecloth@mailbarrow.com</p>
    </section>

    <section class="card card--back">
      <div class="paper-texture" role="img" aria-label="White crumpled paper texture"></div>
      <h2 class="appointment-title">APPOINTMENT</h2>
      <div class="field field--date">
        <span class="field-label">Date  :</span>
        <span class="field-line"></span>
      </div>
      <div class="field field--place">
        <span class="field-label">Place :</span>
        <span class="field-line"></span>
      </div>
      <div class="bands bands--bottom">
        <span class="band-light"></span>
        <span class="band-mid"></span>
        <span class="band-dark"></span>
      </div>
    </section>
  </main>
</body>
</html>
```